Thermostat Screen Design

We need a screen layout design for a new thermostat we're currently developing. If you're not familiar with thermostats, you can see some examples here - http://smart-climate-units-guide.bestpickdigest.com/

We're after the main page design, with icons, colours etc. It needs to be clean, modern and minimalistic. Attached is all components required on the screen. The screen size is 5 inch (diagnol).

The arrows on the screen showcase what happens when you press a button. For example, when you press MODE once you get OFF, press it twice, HEAT, press it 3 times, COOL, etc. This is just for your reference.

You have complete creative license on how you choose to layout the screen, position the components etc, but we require:

- it must be on a 5 inch screen diagnol
- modern, clean and minimalistic
- includes icons and colours
- Intuitive

Let me know if any questions.

```html
<!DOCTYPE html>
<html lang="en">
<head>
<meta charset="utf-8">
<title>Thermostat Main Screen</title>
<link href="https://fonts.googleapis.com/css2?family=Lato:wght@300;400;700&display=swap" rel="stylesheet">
<style>
  :root {
    --page-bg: #54575c;
    --screen-purple: #7a1d98;
    --setpoint-fill: #561068;
    --line-light: #e9d8ef;
    --text-white: #ffffff;
    --text-soft: #eadff0;
    --text-dim: #a46bb8;
    --ghost-digit: #8a3aa6;
  }
  html, body {
    margin: 0;
    width: 1200px;
    height: 1000px;
    overflow: hidden;
    background: var(--page-bg);
    font-family: "Lato", sans-serif;
  }
  .screen {
    position: absolute;
    left: 33px;
    top: 183px;
    width: 1134px;
    height: 634px;
    overflow: hidden;
    background: var(--screen-purple);
    color: var(--text-white);
  }
  .screen > * { position: absolute; margin: 0; }
  .program-mode {
    left: 140px; top: 24px;
    font-size: 28px; letter-spacing: 7px; line-height: 1;
    color: var(--text-soft); font-weight: 400;
  }
  .clock {
    right: 40px; top: 4px;
    text-align: right;
    font-size: 32px; letter-spacing: 6px; line-height: 46px;
    color: var(--text-soft); font-weight: 400;
  }
  .menu-button {
    left: 26px; width: 383px; height: 120px;
    border: 2px solid var(--line-light);
    border-radius: 22px;
    display: flex; align-items: center; justify-content: center;
    font-size: 34px; font-weight: 700; letter-spacing: 12px;
    color: var(--text-white);
  }
  .menu-mode { top: 99px; }
  .menu-fan { top: 226px; }
  .menu-settings { top: 354px; }
  .menu-zone { top: 478px; }
  .setpoint-value {
    left: 430px; width: 174px; height: 115px;
    border: 2px solid var(--line-light);
    border-radius: 14px;
    background: var(--setpoint-fill);
    display: flex; align-items: center; justify-content: center;
    font-size: 76px; font-weight: 300;
  }
  .heat-value { top: 44px; }
  .cool-value { top: 440px; left: 436px; width: 180px; }
  .setpoint-label {
    font-size: 33px; letter-spacing: 8px; line-height: 30px;
    color: var(--text-dim); font-weight: 300;
  }
  .setpoint-label small { display: block; font-size: 17px; letter-spacing: 5px; }
  .heat-label { left: 626px; top: 78px; }
  .cool-label { left: 645px; top: 476px; }
  .ghost-digit {
    left: 462px; top: 188px;
    font-size: 210px; font-weight: 300; line-height: 1;
    color: var(--ghost-digit);
  }
  .room-temp {
    left: 580px; top: 188px;
    font-size: 210px; font-weight: 300; line-height: 1;
  }
  .degree-mark { left: 816px; top: 208px; }
  .room-label {
    left: 470px; top: 400px;
    font-size: 31px; letter-spacing: 15px; line-height: 1;
    color: var(--text-dim); font-weight: 300;
  }
  .zone-name {
    left: 488px; top: 578px;
    font-size: 38px; letter-spacing: 14px; line-height: 1; font-weight: 400;
  }
  .adjust-button {
    left: 868px; width: 220px; height: 122px;
    border: 2px solid var(--line-light);
    display: flex; align-items: center; justify-content: center;
  }
  .adjust-up { top: 104px; }
  .adjust-down { top: 254px; }
  .reading {
    left: 875px; width: 220px; text-align: center;
    font-weight: 400; line-height: 1;
  }
  .outdoor-value { top: 382px; font-size: 90px; }
  .outdoor-label { top: 479px; font-size: 26px; color: var(--text-soft); }
  .humidity-value { top: 511px; font-size: 90px; }
  .humidity-label { top: 598px; left: 855px; font-size: 24px; color: var(--text-soft); }
</style>
</head>
<body>
  <main class="screen">
    <p class="program-mode">SLEEP</p>
    <p class="clock">MAR/23/2014<br>10:45am</p>

    <div class="menu-button menu-mode">MODE</div>
    <div class="menu-button menu-fan">FAN</div>
    <div class="menu-button menu-settings">SETTINGS</div>
    <div class="menu-button menu-zone">ZONE</div>

    <div class="setpoint-value heat-value">90°</div>
    <p class="setpoint-label heat-label">HEAT<small>SETPOINT</small></p>

    <p class="ghost-digit" aria-hidden="true">0</p>
    <p class="room-temp">70</p>
    <svg class="degree-mark" width="36" height="36" viewBox="0 0 36 36" aria-hidden="true"><circle cx="18" cy="18" r="15" fill="none" stroke="#fff" stroke-width="4"/></svg>
    <p class="room-label">Room Temp.</p>

    <div class="setpoint-value cool-value">40°</div>
    <p class="setpoint-label cool-label">COOL<small>SETPOINT</small></p>

    <p class="zone-name">Zone 1</p>

    <div class="adjust-button adjust-up" aria-label="Raise setpoint">
      <svg width="90" height="90" viewBox="0 0 90 90"><rect x="39" y="0" width="12" height="90" fill="#fff"/><rect x="0" y="39" width="90" height="12" fill="#fff"/></svg>
    </div>
    <div class="adjust-button adjust-down" aria-label="Lower setpoint">
      <svg width="40" height="12" viewBox="0 0 40 12"><rect x="0" y="0" width="40" height="12" fill="#fff"/></svg>
    </div>

    <p class="reading outdoor-value">95°</p>
    <p class="reading outdoor-label">Outdoor Temp</p>
    <p class="reading humidity-value">40%</p>
    <p class="reading humidity-label">Indoor RH</p>
  </main>
</body>
</html>
```